Amber Heron Fund Pitch Deck

This is a PowerPoint for use in investor presentations. The copy is written (although it may have small tweaks) and the designer will be responsible for creating a template and some graphical representations inside the presentation.

Note on the logo. Only the Amber Heron should be used, not the text.

```html
<!DOCTYPE html>
<html lang="en">
<head>
<meta charset="utf-8">
<title>Amber Heron Fund – Slide Outline</title>
<link href="https://fonts.googleapis.com/css2?family=Montserrat:wght@300;400;500;600;700&display=swap" rel="stylesheet">
<style>
:root{
  --page:#e4e4e4;
  --blue:#6d8bc6;
  --blue-dark:#5a78b6;
  --band:#98b3df;
  --grey-wedge:#e6e6e6;
  --ink:#3a3a3a;
  --white:#ffffff;
}
*{margin:0;padding:0;box-sizing:border-box}
html,body{width:1200px;height:782px;overflow:hidden;background:var(--page)}
body{position:relative;font-family:'Montserrat',sans-serif;color:var(--ink)}
.slide{position:absolute;width:336px;height:189px;background:var(--white);overflow:hidden;box-shadow:0 1px 3px rgba(0,0,0,.18)}
.s1{left:53px;top:120px}.s2{left:438px;top:120px}.s3{left:810px;top:120px}
.s4{left:53px;top:415px}.s5{left:438px;top:415px}.s6{left:810px;top:415px}
.abs{position:absolute}
.slide-title{position:absolute;left:17px;top:8px;font-weight:300;font-size:8.6px;letter-spacing:.2px;color:var(--blue);text-transform:uppercase}
.footer{position:absolute;left:0;bottom:0;width:100%;height:16px;background:var(--band)}
.footer-tip{position:absolute;right:0;bottom:0;width:10px;height:16px;background:var(--blue);clip-path:polygon(60% 0,100% 0,100% 100%,0 100%)}
.footer-brand{position:absolute;left:17px;top:5px;font-size:3.4px;font-weight:600;color:var(--white);line-height:1.2}
.footer-label{position:absolute;right:17px;top:5.5px;font-size:3.8px;font-weight:300;color:var(--white)}
.footer-label b{font-weight:700}
.body{font-size:4.7px;line-height:1.3;font-weight:400}
.light{color:var(--white)}
.photo{position:absolute}

/* cover */
.cover-rule{left:0;top:12px;width:303px;height:.6px;background:var(--band)}
.cover-diamond{left:123px;top:8px;width:8px;height:8px;background:var(--band);transform:rotate(45deg)}
.cover-photo{left:0;top:78px;width:300px;height:111px;background:linear-gradient(160deg,#c7dca6 0%,#86a65a 45%,#4f6d2c 80%,#b08a44 100%)}
.cover-cut{left:226px;top:103px;width:150px;height:150px;border-radius:50%;background:var(--white)}
.cover-band{left:0;top:36px;width:290px;height:58px;background:var(--blue);border-radius:0 30px 30px 0}
.cover-title{left:61px;top:45px;font-size:9.4px;font-weight:300;color:var(--white);line-height:1.25}
.cover-title b{font-weight:700}
.cover-brand{left:262px;top:152px;font-size:7px;font-weight:600;color:var(--blue)}

/* edge */
.edge-copy{left:17px;top:24px;width:122px}
.edge-accent{left:17px;top:64px;width:116px;font-weight:600;color:var(--blue)}
.edge-photo{left:145px;top:0;width:191px;height:98px;background:linear-gradient(120deg,#9a6f5a 0%,#d9cfc6 45%,#eceae6 70%,#b9a99b 100%)}
.edge-panel{left:108px;top:98px;width:228px;height:75px;background:var(--blue);border-radius:14px 0 0 0}
.edge-stats{left:158px;top:104px;width:116px;color:var(--white);font-size:4.5px;font-weight:600;line-height:1.3}
.stat{font-size:8.4px;font-weight:700;display:block}
.stat small{font-size:3.8px}

/* technology */
.tech-column{left:118px;top:0;width:109px;height:173px;background:var(--blue)}
.tech-icon{position:absolute;top:52px;width:14px;height:14px}
.tech-line{position:absolute;top:58.5px;height:.6px;width:42px;background:var(--band)}
.tech-text{position:absolute;top:78px;width:78px}

/* people */
.people-panel{left:194px;top:0;width:142px;height:173px;background:var(--blue)}
.portrait{position:absolute;top:18px;width:29px;height:29px;border-radius:50%;border:1.2px solid var(--blue);background:linear-gradient(180deg,#b9b4ae,#6a6f78)}
.person{position:absolute;top:53px;font-size:3.1px;line-height:1.35}
.person .name{font-weight:700;color:var(--blue)}
.person .role{font-weight:300;color:var(--blue)}
.person.on-blue .name{color:var(--white)}
.person ul{list-style:none;margin-top:5px}
.person li{position:relative;padding-left:3.5px;margin-bottom:3px;font-weight:400}
.person li::before{content:"•";position:absolute;left:0}
.person.on-blue li{color:var(--white);font-weight:300}

/* market */
.market-panel{left:0;top:22px;width:116px;height:106px;background:var(--blue);border-radius:0 9px 9px 0}
.market-figures{left:17px;top:31px;width:92px;color:var(--white);font-size:5.4px;font-weight:300;line-height:1.3}
.market-figures b{display:block;font-size:7.6px;font-weight:700;margin-top:11px}
.market-figures b.second{margin-top:0}
.market-copy{left:129px;top:32px;width:150px;font-size:4.8px;line-height:1.25}
.market-copy .growth{font-weight:700;color:var(--blue);margin-bottom:5px}
.market-photo{left:104px;top:90px;width:232px;height:83px;background:linear-gradient(100deg,#d9d3cc 0%,#efe9e2 40%,#c9c4bf 70%,#8e8a87 100%)}

/* process */
.process-graphic{left:0;top:0;width:336px;height:173px}
.process-title{color:var(--white)}
.step{position:absolute;font-size:3.9px;line-height:1.3;font-weight:400}
.step::before{content:"";display:block;width:14px;height:.6px;background:var(--blue);margin-bottom:2px}
.step.right-align{text-align:right}
.step.right-align::before{margin-left:auto}
.step.center{text-align:center}
.step.center::before{margin:0 auto 2px}
.process-brand{left:142px;top:90px;width:52px;text-align:center;font-size:5px;font-weight:600;color:var(--blue)}
</style>
</head>
<body>

<section class="slide s1">
  <div class="abs cover-rule"></div>
  <div class="abs cover-diamond"></div>
  <div class="photo cover-photo" role="img" aria-label="Young plants growing from rising stacks of gold coins"></div>
  <div class="abs cover-cut"></div>
  <div class="abs cover-band"></div>
  <h1 class="abs cover-title">Amber Heron<br>NPL Fund, | <b>Slide Outline</b></h1>
  <div class="abs cover-brand">The Harbor Office</div>
</section>

<section class="slide s2">
  <h2 class="slide-title">The Edge</h2>
  <p class="abs body edge-copy">Experience with fund management and asset disposal. Utilizing the clues and hints that borrowers and guarantors leave on the Internet, we can special service assets and collect on them more quickly and maximize return.</p>
  <p class="abs body edge-accent">Much of the technology and experience as a team can be attributed to the team's experience at Tallowbrook.</p>
  <div class="photo edge-photo" role="img" aria-label="Two business colleagues giving a high five in an office"></div>
  <div class="abs edge-panel"></div>
  <div class="abs edge-stats">
    The principals were the management team that came on in March 2020 and grew the business from:<br><br>
    less than
    <span class="stat">12,000 PPP <small>loans</small></span>
    <br>to more than
    <span class="stat">800,000.</span>
  </div>
  <footer class="footer"><span class="footer-brand">The Harbor Office</span><span class="footer-label">Amber Heron NPL Fund, | <b>Slide Outline</b></span><span class="footer-tip"></span></footer>
</section>

<section class="slide s3">
  <h2 class="slide-title">The Technology</h2>
  <div class="abs tech-column"></div>
  <svg class="tech-icon" style="left:17px" viewBox="0 0 14 14"><circle cx="7" cy="7" r="7" fill="#6d8bc6"/><rect x="4.5" y="3.5" width="4.5" height="6" fill="none" stroke="#fff" stroke-width=".6"/><line x1="5.3" y1="5.2" x2="8.2" y2="5.2" stroke="#fff" stroke-width=".5"/><line x1="5.3" y1="6.6" x2="8.2" y2="6.6" stroke="#fff" stroke-width=".5"/><circle cx="9.2" cy="9.6" r="1.3" fill="none" stroke="#fff" stroke-width=".5"/></svg>
  <div class="tech-line" style="left:52px"></div>
  <svg class="tech-icon" style="left:129px" viewBox="0 0 14 14"><circle cx="7" cy="7" r="6.7" fill="#6d8bc6" stroke="#fff" stroke-width=".5"/><circle cx="6.3" cy="6.3" r="2.3" fill="none" stroke="#fff" stroke-width=".6"/><line x1="8" y1="8" x2="10" y2="10" stroke="#fff" stroke-width=".7"/></svg>
  <div class="tech-line" style="left:165px"></div>
  <svg class="tech-icon" style="left:234px" viewBox="0 0 14 14"><circle cx="7" cy="7" r="7" fill="#98b3df"/><text x="7" y="8.6" text-anchor="middle" font-family="Montserrat,sans-serif" font-size="4" fill="#fff">$$$</text></svg>
  <p class="tech-text body" style="left:17px">Most lenders and servicers use Ledgervale or Loanwright and then software like Dunmere Collect for collections.</p>
  <p class="tech-text body light" style="left:129px;width:86px;font-weight:300">These software packages fail to address the most important factors which is to analyze the borrower (and the guarantors) to allow for customized collection plans. We use enhanced skip tracing developed during PPP forgiveness and collection efforts with advanced social media logic.</p>
  <p class="tech-text body" style="left:234px;width:88px">Finally, we use evolving algorithms to price and purchase NPL portfolios at the correct price.</p>
  <footer class="footer"><span class="footer-brand">The Harbor Office</span><span class="footer-label">Amber Heron NPL Fund, | <b>Slide Outline</b></span><span class="footer-tip"></span></footer>
</section>

<section class="slide s4">
  <h2 class="slide-title">The People</h2>
  <div class="abs people-panel"></div>
  <div class="portrait" role="img" aria-label="Headshot portrait" style="left:17px"></div>
  <div class="portrait" role="img" aria-label="Headshot portrait" style="left:78px"></div>
  <div class="portrait" role="img" aria-label="Headshot portrait" style="left:139px"></div>
  <div class="portrait" role="img" aria-label="Headshot portrait" style="left:201px;border-color:#fff"></div>
  <div class="portrait" role="img" aria-label="Headshot portrait" style="left:267px;border-color:#fff"></div>

  <div class="person" style="left:17px;width:50px">
    <span class="name">Graham Colter,</span> <span class="role">Managing Partner, Investment Committee</span>
    <ul>
      <li>More than 20 years of banking experience with three national banks</li>
      <li>Director of Larrow Capital Management, in less than 5 years, achieved 4x AUM and outsized returns managing distressed asset fund. Developed framework for additional funds.</li>
      <li>CEO of Tallowbrook.</li>
    </ul>
  </div>
  <div class="person" style="left:78px;width:54px">
    <span class="name">Julian Farrow,</span><br><span class="role">Managing Partner, Investment Committee</span>
    <ul>
      <li>Founder of Ridgemoor Law in Scottsdale, Arizona which became the first law firm in the country sold to private non-lawyer investors.</li>
      <li>Extensive experience with large transactions including leading the largest 2017 Arizona transaction on behalf of a client. Known for liquidation sales inside bankruptcy. Speaker at National Insolvency Forum conference in Las Vegas.</li>
      <li>COO of Quenloft, an early web development company that first implemented a commercially successful e-commerce campaign.</li>
      <li>General Counsel of Tallowbrook.</li>
    </ul>
  </div>
  <div class="person" style="left:139px;width:52px">
    <span class="name">Evan Delacroix,</span> <span class="role">Investment Committee</span>
    <ul>
      <li>CEO of Crosswell Impact Corp.</li>
      <li>CEO, Kestrelwood Bank</li>
      <li>Director, Halvern Bank</li>
      <li>Member, Civic Directors Forum</li>
    </ul>
  </div>
  <div class="person on-blue" style="left:201px;width:56px">
    <span class="name">Daniel Rask, Director of Credit Analytics.</span>
    <ul>
      <li>Product and data specialist with more than 15 years technology and startup experience.</li>
      <li>Founded Dovrelink Communications, which combined email and chat for customer success professionals. Raised $5 million capital and had more than 40,000 users.</li>
      <li>Led advertising products at Brindlestack and grew from $7 million to $45 million in revenue over 5 years.</li>
      <li>Advisory Board member with well-known venture capital firm.</li>
      <li>VP, Products, Tallowbrook.</li>
    </ul>
  </div>
  <div class="person on-blue" style="left:267px;width:56px">
    <span class="name">Miles Yarrow, Chief Operating Officer</span>
    <ul>
      <li>Management Consultant at Ashgrove &amp; Partners</li>
      <li>Founder of two companies that grew to more than 1,000 employees.</li>
      <li>COO of Tallowbrook.</li>
    </ul>
  </div>
  <footer class="footer"><span class="footer-brand">The Harbor Office</span><span class="footer-label">Amber Heron NPL Fund, | <b>Slide Outline</b></span><span class="footer-tip"></span></footer>
</section>

<section class="slide s5">
  <h2 class="slide-title">The Market</h2>
  <div class="abs market-panel"></div>
  <div class="abs market-figures">
    The commercial lending market size was valued at
    <b>$8,823.53</b>billion in 2020,<br><br>
    and is projected to reach
    <b class="second">$29,379.83</b>billion by 2030,
  </div>
  <div class="abs market-copy">
    <p class="growth">Growing at a CAGR of 13.1% from 2021 to 2030.</p>
    <p>Source:<br>https://www.brantlywoodresearch.com/commercial-lendi<br>ng-market-report</p>
    <p style="margin-top:5px">The credit cycle is entering into a period of rising interest rates and corresponding defaults. The fund seeks to take advantage of that emerging opportunity.</p>
  </div>
  <div class="photo market-photo" role="img" aria-label="Two people reviewing and signing loan documents at a desk"></div>
  <footer class="footer"><span class="footer-brand">The Harbor Office</span><span class="footer-label">Amber Heron NPL Fund, | <b>Slide Outline</b></span><span class="footer-tip"></span></footer>
</section>

<section class="slide s6">
  <svg class="abs process-graphic" viewBox="0 0 336 173" aria-hidden="true">
    <polygon points="208,0 336,0 336,173 166,173" fill="#e6e6e6"/>
    <polygon points="0,0 115,0 0,109" fill="#6d8bc6"/>
    <circle cx="168" cy="94" r="40" fill="none" stroke="#98b3df" stroke-width="2"/>
    <g fill="#6d8bc6" stroke="#fff" stroke-width="1">
      <circle cx="168" cy="53" r="7"/>
      <circle cx="194" cy="63" r="6.5"/>
      <circle cx="207" cy="97" r="6.5"/>
      <circle cx="194" cy="126" r="6.5"/>
      <circle cx="141" cy="126" r="6.5"/>
      <circle cx="126" cy="97" r="6.5"/>
      <circle cx="141" cy="63" r="6.5"/>
    </g>
    <g fill="none" stroke="#fff" stroke-width=".6">
      <circle cx="166" cy="52" r="1.4"/><circle cx="170" cy="52" r="1.4"/><path d="M163 57q3-3 5 0q2-3 5 0"/>
      <line x1="192" y1="61" x2="192" y2="66"/><line x1="196" y1="61" x2="196" y2="66"/><line x1="192" y1="63.5" x2="196" y2="63.5"/>
      <circle cx="207" cy="97" r="3"/><circle cx="207" cy="97" r="1.2"/>
      <path d="M190 125h8M191 125v3M194 125v3M197 125v3M190 128h8M190 125l4-2 4 2"/>
      <path d="M138 127l2-2 2 1 2-2M137 125l2 2"/>
      <path d="M126 94l3 1v2.5q0 2-3 3.5q-3-1.5-3-3.5v-2.5z"/>
      <rect x="138.5" y="60.5" width="4" height="5"/><line x1="139.5" y1="62" x2="141.5" y2="62"/><line x1="139.5" y1="63.5" x2="141.5" y2="63.5"/>
    </g>
  </svg>
  <h2 class="slide-title process-title">Our Process</h2>
  <div class="abs process-brand">Amber Heron</div>
  <p class="step center" style="left:141px;top:14px;width:54px">Work with our lender customers on their non-performing loan portfolio.</p>
  <p class="step" style="left:209px;top:50px;width:52px">Purchase participation in non-performing loans.</p>
  <p class="step" style="left:222px;top:87px;width:60px">Provide special servicing in compliance with bank's servicing criteria.</p>
  <p class="step" style="left:186px;top:136px;width:54px">Provide bank access to NPL platform.</p>
  <p class="step right-align" style="left:84px;top:136px;width:54px">Maintain first right of refusal to purchase loan using proprietary algorithm.</p>
  <p class="step right-align" style="left:60px;top:82px;width:47px">Internal servicing standards.</p>
  <p class="step right-align" style="left:74px;top:49px;width:48px">Liquidation, when necessary.</p>
  <footer class="footer"><span class="footer-brand">The Harbor Office</span><span class="footer-label">Amber Heron NPL Fund, | <b>Slide Outline</b></span><span class="footer-tip"></span></footer>
</section>

</body>
</html>
```